Pyramide TAGESFLUSS
Zielgruppe
Tobias Rahnfeld ist... Der Mann mit dem roten Stirnband (www.sonnenkreis-beispiel.de)
Videoinfo (BITTE UNBEDINGT ANSCHAUEN) unter:
http://www.clipvora.com/watch?v=pQ7mwe3tz8a
Er ist die Personifizierung eines eigenverantwortlichen und selbstbestimmten Lebens. Seit mehr als 15 Jahren beschäftigt er sich mit der Psychologie des Erfolgs und den Gesetzen des Lebens. Er entwickelte die Pyramide TAGESFLUSS und ist Urheber des Konzeptes SONNENKREIS WACHSEN.
Einzigartigkeit hat Tobias Rahnfeld schon früh erfahren. Im Alter von 16 war er nicht nur der jüngste Spieler in der Korbball-Oberklasse, sondern neun Jahre später auch einer der jüngsten Korbball-Oberklasse-Cheftrainer in der Geschichte dieses Sports. Er hat mit Jens Haverkamp zusammen gespielt, zwei Europameisterschaften für die deutsche Junioren-Nationalmannschaft absolviert und eine Europameisterschaft als Trainer gecoacht.
Parallel zu seiner Trainerkarriere hat Rahnfeld das BWL-Studium erfolgreich abgeschlossen. Darüber hinaus konnte er von Weltklasse-Nationaltrainern wie Uwe Leitgeber (Deutschland) oder Todd Wanamaker (USA) lernen, was Führungsstärke und -intelligenz bedeutet.
+++ Welche Produkte bieten wir an? -> Seminare, Vorträge und Bücher/Hörbücher +++
Tobias Rahnfeld steht für Erfolg, Glück und Erfüllung. Heute gibt er seine Expertise als gefragter Referent national und international an viele Menschen in Unternehmen aller Branchen weiter. Seine Seminarreihe SONNENKREIS WACHSEN mit den Events DER MUT, DEINEN WEG ZU GEHEN (www.tobias-rahnfeld.com/dermut), TATENDRANG Das Denken auf Ziele ausrichten (http://www.tobias-rahnfeld.com/events-tatendrang) und INNENSTÄRKE Freude und Sinn gestalten (www.tobias-rahnfeld.com/innenstaerke) hat sich in der Spitze der Persönlichkeitsentwicklung etabliert. Sie vermittelt Privatpersonen aller Altersklassen das Wissen, die mentalen Fähigkeiten und umsetzbaren Stra..
Aufgabenstellung
Es geht darum, die bereits bestehende Pyramide (zu sehen unter: http://www.tobias-rahnfeld.com/de/konzept) in eine neue "Form" zu bringen, die unserer gesamten CI/CD besser entspricht als die jetzige Variante. Sie muss/darf nicht wirklich ein Kunstwerk werden, sollte jedoch insgesamt dem Stil unseres Auftrittes entsprechen. Sie wird sowohl in Vorträgen und Seminaren an der Leinwand vor etlichen Leuten zu sehen sein, als auch auf der Website und in unseren Kommunikationsmaterialien Verwendung finden.
Zu den Reglern:
Modern - sie darf nicht zu modern sein, sollte jedoch auch nicht zu klassisch daher kommen. Die Zielgruppe sind Menschen von jung bis alt. Es geht hier nicht darum, eine spezielle Zielgruppe anzusprechen, sondern eher, eine einprägsame und schnell verständliche sowie übersichtliche Pyramide zu gestallten.
Exklusiv - kein Kommentar dazu. Eher im Mittelfeld.
Verspielt - weder noch. Zielgruppe ist weit gefasst, von daher muss auch die Pyramide vielen Menschen gefallen und sie muss ansprechend dargestellt werden.
Einfarbig: Es müssen die CI-Farben verwendet werden. Wichtig!
LAB: 38 63 37 - CMYK: 020 100 085 010 - RGB: 184 0 34 - HEX: B80022
Typo: Helvetica Neue LT Std

```html
<!DOCTYPE html>
<html lang="de">
<head>
<meta charset="utf-8">
<title>Pyramide TAGESFLUSS</title>
<link rel="stylesheet" href="https://fonts.googleapis.com/css2?family=Inter:wght@300;400;500;700&display=swap">
<style>
  :root {
    --ci-red: #b80022;
    --level-1: #b80022;
    --level-2: #c01a39;
    --level-3: #c52e48;
    --level-4: #cb4459;
    --level-5: #d25b6c;
    --level-6: #da7381;
    --level-7: #e499a4;
    --number: #d9707f;
    --frame: #e2a3ad;
    --paper: #ffffff;
    --block-w: 133.2px;
    --block-h: 65px;
    --gap: 2.4px;
  }
  * { box-sizing: border-box; margin: 0; padding: 0; }
  html, body { width: 1200px; height: 660px; overflow: hidden; background: var(--paper); }
  body { font-family: "Inter", "Helvetica Neue", Arial, sans-serif; position: relative; }

  .frame {
    position: absolute; left: 56px; top: 50px; width: 1088px; height: 560px;
    border: 1px solid var(--frame);
  }

  .legend {
    position: absolute; left: 90px; top: 80px; list-style: none;
    color: var(--ci-red); font-size: 15px; line-height: 24px; letter-spacing: 0.2px;
  }

  .title {
    position: absolute; right: 90px; top: 78px; text-align: right;
    color: var(--ci-red); font-weight: 700; font-size: 36px; line-height: 38px; letter-spacing: 0.3px;
  }

  .level {
    position: absolute; display: flex; gap: var(--gap); height: var(--block-h);
  }
  .block {
    width: var(--block-w); height: 100%;
    display: flex; align-items: center; justify-content: center;
    color: #fff; font-size: 14.5px; letter-spacing: 0.6px; white-space: nowrap;
  }
  .level-number {
    position: absolute; right: calc(100% + 22px); top: 50%; transform: translateY(-50%);
    color: var(--number); font-size: 28px; font-weight: 300;
  }

  .level-7 { left: 568px; top: 85px; }   .level-7 .block { background: var(--level-7); }
  .level-6 { left: 499px; top: 154px; }  .level-6 .block { background: var(--level-6); }
  .level-5 { left: 431px; top: 221px; }  .level-5 .block { background: var(--level-5); }
  .level-4 { left: 362px; top: 289px; }  .level-4 .block { background: var(--level-4); }
  .level-3 { left: 295px; top: 356px; }  .level-3 .block { background: var(--level-3); }
  .level-2 { left: 227px; top: 425px; }  .level-2 .block { background: var(--level-2); }

  .level-1 { left: 158px; top: 492px; width: 952px; height: 66px; }
  .foundation {
    width: 100%; height: 100%; background: var(--level-1);
    display: flex; align-items: center; justify-content: space-between;
    padding: 0 42px 0 38px;
    color: #fff; font-size: 34px; font-weight: 300;
  }

  .website {
    position: absolute; right: 90px; top: 576px;
    display: flex; align-items: center; gap: 10px;
    color: var(--ci-red); font-weight: 700; font-size: 14px; letter-spacing: 0.3px;
  }
</style>
</head>
<body>
  <div class="frame"></div>

  <ol class="legend">
    <li>1. BASISEBENE/FUNDAMENT</li>
    <li>2. MENTALEBENE</li>
    <li>3. HANDLUNGSEBENE</li>
    <li>4. WISSENSEBENE</li>
    <li>5. DEFINITIONSEBENE</li>
    <li>6. SOZIALEBENE</li>
    <li>7. SINNEBENE</li>
  </ol>

  <h1 class="title">SONNENKREIS<br>WACHSEN</h1>

  <div class="level level-7"><span class="level-number">7.</span>
    <div class="block">Sinn</div>
  </div>
  <div class="level level-6"><span class="level-number">6.</span>
    <div class="block">Umfeld</div><div class="block">Umgang</div>
  </div>
  <div class="level level-5"><span class="level-number">5.</span>
    <div class="block">Werte</div><div class="block">Selbstbild</div><div class="block">Regeln</div>
  </div>
  <div class="level level-4"><span class="level-number">4.</span>
    <div class="block">Beruf</div><div class="block">Partnerschaft</div><div class="block">Gesundheit</div><div class="block">Geld</div>
  </div>
  <div class="level level-3"><span class="level-number">3.</span>
    <div class="block">Disziplin</div><div class="block">Prioritäten</div><div class="block">Ziele</div><div class="block">Ausdauer</div><div class="block">Neugier</div>
  </div>
  <div class="level level-2"><span class="level-number">2.</span>
    <div class="block">Emotionen</div><div class="block">Gedanken</div><div class="block">Selbstvertrauen</div><div class="block">Überzeugungen</div><div class="block">Fokus</div><div class="block">Spiritualität</div>
  </div>
  <div class="level level-1"><span class="level-number">1.</span>
    <div class="foundation" aria-label="Eigenverantwortung">
      <span>E</span><span>I</span><span>G</span><span>E</span><span>N</span><span>V</span><span>E</span><span>R</span><span>A</span><span>N</span><span>T</span><span>W</span><span>O</span><span>R</span><span>T</span><span>U</span><span>N</span><span>G</span>
    </div>
  </div>

  <div class="website">
    <svg width="7" height="10" viewBox="0 0 7 10" aria-hidden="true"><polygon points="0,0 7,5 0,10" fill="#b80022"/></svg>
    <span>WWW.SONNENKREIS-BEISPIEL.DE</span>
  </div>
</body>
</html>
```